Fastest Work at home Solution for Small Businesses

We need a web page for a product called *CopperVale*
We develop an innovative VPN Appliance (Model-Name ->Vale Nine) that gives small business the possibility literally setup the possibility for Companies to let their employees work from home.
With our secure appliance we create safe connection between any business and the employee *working at home*
Our Products *Vale Nine* are rolled out in minutes.
A. Employees can connect directly
B. Work from any location
C. All this without having to change the company firewall
Use case
=======
1. Go to our page
2. Select Product
3. Order
4. Connect to any Switch in the company
5. install software on employees laptop
***** INSTANT Connection ******
Businesses

```html
<!DOCTYPE html>
<html lang="en">
<head>
<meta charset="utf-8">
<title>CopperVale – Work at Home Solution</title>
<link href="https://fonts.googleapis.com/css2?family=Poppins:wght@300;400;500;600;700;800&display=swap" rel="stylesheet">
<style>
:root{
  --navy:#0b2a5c;
  --ink:#141414;
  --royal:#0646b8;
  --royal-deep:#0a3aa6;
  --sky:#5dd3f6;
  --frame:#4fcdf3;
  --muted:#6e6e6e;
  --ghost:#e6e6e6;
  --dot-field:#eef1f6;
  --footer:#f3f3f3;
  --line:#bdbdbd;
}
*{margin:0;padding:0;box-sizing:border-box}
html,body{width:1200px;height:4346px;overflow:hidden;background:#fff}
body{position:relative;font-family:'Poppins',sans-serif;color:var(--ink)}
.abs{position:absolute}
.brand{display:flex;align-items:center;gap:12px;font-weight:700;color:var(--navy);letter-spacing:-.5px}
.brand-mark{width:30px;height:30px;background:var(--royal);border-radius:4px}
.site-header .brand{left:89px;top:20px;font-size:40px}
.main-nav{top:36px;left:0;width:1200px;font-size:15px;color:#333}
.main-nav a{position:absolute;text-decoration:none;color:#333;white-space:nowrap}
.main-nav a.active{color:var(--sky)}
.btn{display:flex;align-items:center;justify-content:center;background:var(--royal);color:#fff;font-weight:600;font-size:16px;border-radius:3px;text-decoration:none}
.hero-title{left:90px;top:140px;width:420px;font-size:43px;line-height:47px;font-weight:800;color:var(--navy)}
.hero-copy{left:90px;top:303px;width:381px;font-size:16px;line-height:32px;color:#444;text-align:justify;font-weight:300}
.dot-field{background:var(--dot-field);border-radius:6px}
.photo{border-radius:34px}
.section-title{left:0;width:1200px;text-align:center;font-weight:700;font-size:40px;color:var(--ink)}
.section-sub{left:0;width:1200px;text-align:center;font-size:18px;color:var(--royal)}
.blue-block{background:var(--royal);border-radius:0 0 14px 0}
.blue-block.right{border-radius:0 0 0 14px}
.photo-frame{background:var(--frame);border-radius:34px}
.photo-frame .photo{position:absolute;top:0;right:0;border-radius:34px}
.step-num{font-size:190px;line-height:1;font-weight:700;color:var(--ghost);letter-spacing:-6px}
.step-title{font-size:37px;line-height:41px;font-weight:500;color:var(--ink)}
.step-copy{font-size:15.5px;line-height:27.7px;color:var(--muted);font-weight:300}
.usecase .brand{left:89px;top:2804px;font-size:30px}
.usecase-arrows{left:89px;top:3016px;display:flex;gap:8px}
.case-card{top:2795px;height:238px;background:linear-gradient(180deg,#0b58d0 0%,#0a3fb0 100%);color:#fff;font-weight:600;font-size:18px;line-height:20px}
.case-card svg{position:absolute;left:14px;top:16px}
.case-card span{position:absolute;left:14px;bottom:14px;right:10px}
.testimonial{width:330px;text-align:center}
.avatar{width:80px;height:80px;border-radius:50%;margin:0 auto;background:radial-gradient(circle at 50% 40%,#c89a82,#6d5447)}
.testimonial p{margin-top:20px;font-size:14px;line-height:27.5px;color:var(--muted);font-weight:300}
.testimonial cite{display:block;margin-top:9px;font-style:normal;font-weight:600;font-size:14px;color:var(--royal)}
.contact-title{left:90px;top:3571px;font-size:40px;font-weight:700}
.field{border:1px solid var(--line);font-size:15px;color:#777;padding:0 10px;display:flex;align-items:center;font-weight:300}
.field.message{align-items:flex-start;padding-top:10px}
.site-footer{left:0;top:4122px;width:1200px;height:224px;background:var(--footer)}
.site-footer .brand{left:0;width:1200px;justify-content:center;top:76px;font-size:44px}
.footer-nav a{position:absolute;top:149px;font-size:14px;color:#444;text-decoration:none}
.copyright{top:193px;width:1200px;text-align:center;font-size:12px;color:#777}
</style>
</head>
<body>

<header class="site-header">
  <div class="abs brand"><span class="brand-mark"></span>CopperVale</div>
  <nav class="abs main-nav">
    <a href="#" class="active" style="left:663px">HOME</a>
    <a href="#" style="left:760px">ABOUT US</a>
    <a href="#" style="left:888px">SERVICES</a>
    <a href="#" style="left:1010px">CONTACT US</a>
  </nav>
</header>

<section class="hero">
  <h1 class="abs hero-title">Fastest Work at home Solution for Small Businesses</h1>
  <p class="abs hero-copy">Lorem ipsum dolor sit amet, consectetur adipiscing elit, sed do eiusmod tempor incididunt ut labore et dolore magna aliqua. Ut enim ad minim veniam, quis nostrud exercitation ullamco laboris nisi ut aliquip ex ea commodo consequat.</p>
  <a href="#" class="abs btn" style="left:90px;top:525px;width:168px;height:49px">Get Started</a>
  <div class="abs dot-field" role="img" aria-label="Dot grid decoration" style="left:586px;top:121px;width:190px;height:166px"></div>
  <div class="abs" style="left:645px;top:240px;width:390px;height:398px;background:var(--sky);border-radius:34px"></div>
  <div class="abs" role="img" aria-label="Smiling woman in a white shirt holding an open laptop" style="left:530px;top:76px;width:470px;height:562px;background:linear-gradient(180deg,rgba(240,236,232,.85) 0%,rgba(200,205,212,.7) 55%,rgba(40,70,110,.75) 100%);border-radius:40px 40px 30px 30px"></div>
</section>

<section class="products">
  <h2 class="abs section-title" style="top:725px">Our Products</h2>
  <div class="abs section-sub" style="top:780px">Vale Nine</div>

  <div class="abs blue-block" style="left:0;top:1168px;width:127px;height:233px"></div>
  <div class="abs dot-field" role="img" aria-label="Dot grid decoration" style="left:37px;top:822px;width:187px;height:236px"></div>
  <div class="abs photo-frame" style="left:81px;top:861px;width:495px;height:469px">
    <div class="photo" role="img" aria-label="Woman at a desk on a video call with colleagues" style="left:8px;width:487px;height:461px;background:linear-gradient(135deg,#c9d3b4 0%,#e6d3c6 45%,#6b5a4d 100%)"></div>
  </div>
  <div class="abs step-num" style="left:646px;top:850px">01</div>
  <h3 class="abs step-title" style="left:646px;top:948px;width:460px">Employees can connect directly</h3>
  <p class="abs step-copy" style="left:645px;top:1055px;width:460px">Lorem ipsum dolor sit amet, consectetur adipiscing elit, sed do eiusmod tempor incididunt ut labore et dolore magna aliqua. Ut enim ad minim veniam, quis nostrud exercitation ullamco laboris nisi ut aliquip ex ea commodo consequat. Duis aute irure dolor in reprehenderit in voluptate velit esse cillum dolore eu fugiat nulla pariatur.</p>
  <a href="#" class="abs btn" style="left:646px;top:1249px;width:168px;height:49px">Read More</a>

  <div class="abs blue-block right" style="left:1070px;top:1779px;width:130px;height:235px"></div>
  <div class="abs dot-field" role="img" aria-label="Dot grid decoration" style="left:970px;top:1431px;width:188px;height:240px"></div>
  <div class="abs photo-frame" style="left:621px;top:1472px;width:495px;height:469px">
    <div class="photo" role="img" aria-label="Woman sitting on a rug in a bright living room with a laptop" style="left:0;right:8px;width:487px;height:461px;background:linear-gradient(135deg,#dfe3e0 0%,#c8cfcc 50%,#8c8f93 100%)"></div>
  </div>
  <div class="abs step-num" style="left:93px;top:1461px">02</div>
  <h3 class="abs step-title" style="left:92px;top:1560px;width:460px">Work from any location</h3>
  <p class="abs step-copy" style="left:90px;top:1667px;width:460px">Lorem ipsum dolor sit amet, consectetur adipiscing elit, sed do eiusmod tempor incididunt ut labore et dolore magna aliqua. Ut enim ad minim veniam, quis nostrud exercitation ullamco laboris nisi ut aliquip ex ea commodo consequat. Duis aute irure dolor in reprehenderit in voluptate velit esse cillum dolore eu fugiat nulla pariatur.</p>
  <a href="#" class="abs btn" style="left:91px;top:1860px;width:169px;height:49px">Read More</a>

  <div class="abs blue-block" style="left:0;top:2390px;width:127px;height:235px"></div>
  <div class="abs dot-field" role="img" aria-label="Dot grid decoration" style="left:37px;top:2042px;width:187px;height:237px"></div>
  <div class="abs photo-frame" style="left:81px;top:2083px;width:495px;height:469px">
    <div class="photo" role="img" aria-label="Man on a phone call taking notes beside a laptop at home" style="left:8px;width:487px;height:461px;background:linear-gradient(135deg,#d9c9b2 0%,#e8e2da 50%,#7d6e60 100%)"></div>
  </div>
  <div class="abs step-num" style="left:646px;top:2072px">03</div>
  <h3 class="abs step-title" style="left:646px;top:2170px;width:480px">All this without having to change the company firewall</h3>
  <p class="abs step-copy" style="left:645px;top:2326px;width:460px">Lorem ipsum dolor sit amet, consectetur adipiscing elit, sed do eiusmod tempor incididunt ut labore et dolore magna aliqua. Ut enim ad minim veniam, quis nostrud exercitation ullamco laboris nisi ut aliquip ex ea commodo consequat.</p>
  <a href="#" class="abs btn" style="left:646px;top:2471px;width:168px;height:49px">Read More</a>
</section>

<section class="usecase">
  <h2 class="abs section-title" style="top:2718px">Use Case</h2>
  <div class="abs brand"><span class="brand-mark" style="width:24px;height:24px"></span>CopperVale</div>
  <div class="abs usecase-arrows">
    <svg width="18" height="14" viewBox="0 0 18 14"><path d="M17 7H2M7 2L2 7l5 5" stroke="#999" stroke-width="2.4" fill="none"/></svg>
    <svg width="18" height="14" viewBox="0 0 18 14"><path d="M1 7h15M11 2l5 5-5 5" stroke="#0646b8" stroke-width="2.4" fill="none"/></svg>
  </div>
  <div class="abs case-card" style="left:307px;width:216px">
    <svg width="60" height="66" viewBox="0 0 60 66" fill="none" stroke="#fff" stroke-width="2"><rect x="4" y="6" width="52" height="40" rx="2"/><path d="M4 14h52M22 46v10h16V46M16 58h28"/><circle cx="30" cy="30" r="8"/></svg>
    <span>Go to our page</span></div>
  <div class="abs case-card" style="left:538px;width:217px">
    <svg width="60" height="66" viewBox="0 0 60 66" fill="none" stroke="#fff" stroke-width="2"><rect x="4" y="4" width="52" height="44" rx="2"/><rect x="10" y="12" width="12" height="10"/><rect x="26" y="12" width="12" height="10"/><rect x="10" y="28" width="12" height="10"/><rect x="26" y="28" width="12" height="10"/></svg>
    <span>Select Product</span></div>
  <div class="abs case-card" style="left:770px;width:216px">
    <svg width="60" height="66" viewBox="0 0 60 66" fill="none" stroke="#fff" stroke-width="2"><rect x="10" y="4" width="34" height="52" rx="2"/><path d="M17 16h20M17 24h20M17 32h20M17 40h12M50 8v48"/></svg>
    <span>Order</span></div>
  <div class="abs case-card" style="left:1003px;width:197px">
    <svg width="64" height="66" viewBox="0 0 64 66" fill="none" stroke="#fff" stroke-width="2"><rect x="18" y="4" width="28" height="18"/><path d="M32 22v10M10 32h44M10 32v8M32 32v8M54 32v8"/><rect x="3" y="40" width="14" height="10"/><rect x="25" y="40" width="14" height="10"/><rect x="47" y="40" width="14" height="10"/></svg>
    <span>Connect to any Switch in the company</span></div>
</section>

<section class="testimonials">
  <h2 class="abs section-title" style="top:3120px">Testimonials</h2>
  <figure class="abs testimonial" style="left:75px;top:3196px">
    <div class="avatar" role="img" aria-label="Client portrait"></div>
    <p>Lorem ipsum dolor sit amet, consectetur adipiscing elit, sed do eiusmod tempor incididunt ut labore et dolore</p>
    <cite>-Jolenfield</cite>
  </figure>
  <figure class="abs testimonial" style="left:434px;top:3196px">
    <div class="avatar" role="img" aria-label="Client portrait"></div>
    <p>Lorem ipsum dolor sit amet, consectetur adipiscing elit, sed do eiusmod tempor incididunt ut labore et dolore</p>
    <cite>-Jolenfield</cite>
  </figure>
  <figure class="abs testimonial" style="left:794px;top:3196px">
    <div class="avatar" role="img" aria-label="Client portrait"></div>
    <p>Lorem ipsum dolor sit amet, consectetur adipiscing elit, sed do eiusmod tempor incididunt ut labore et dolore</p>
    <cite>-Jolenfield</cite>
  </figure>
</section>

<section class="contact">
  <h2 class="abs contact-title">Contact Us</h2>
  <div class="abs field" style="left:90px;top:3658px;width:271px;height:40px">Last Name</div>
  <div class="abs field" style="left:373px;top:3658px;width:273px;height:40px">Last Name</div>
  <div class="abs field" style="left:90px;top:3713px;width:271px;height:41px">Phone Number</div>
  <div class="abs field" style="left:373px;top:3713px;width:273px;height:41px">Email</div>
  <div class="abs field" style="left:90px;top:3768px;width:271px;height:42px">Address</div>
  <div class="abs field" style="left:373px;top:3768px;width:273px;height:42px">Subject</div>
  <div class="abs field message" style="left:90px;top:3822px;width:556px;height:108px">Message</div>
  <a href="#" class="abs btn" style="left:90px;top:3943px;width:168px;height:47px">Submit</a>
  <div class="abs dot-field" role="img" aria-label="Dot grid decoration" style="left:992px;top:3489px;width:184px;height:236px"></div>
  <div class="abs photo" role="img" aria-label="Woman writing notes in front of a desktop video call" style="left:663px;top:3550px;width:444px;height:474px;background:linear-gradient(135deg,#e9dfdc 0%,#d9cfd2 50%,#8a7f83 100%)"></div>
</section>

<footer class="abs site-footer">
  <div class="abs brand"><span class="brand-mark" style="width:34px;height:34px"></span>CopperVale</div>
  <nav class="footer-nav">
    <a href="#" style="left:376px">HOME</a>
    <a href="#" style="left:473px">ABOUT US</a>
    <a href="#" style="left:602px">SERVICES</a>
    <a href="#" style="left:724px">CONTACT US</a>
  </nav>
  <p class="abs copyright">© Copyright 2021 The Company name. All Rights Reserved.</p>
</footer>

</body>
</html>
```